Marrowgate Auctions Business Cards Design Needed

I need a business card design that is modern looking - double sided (maybe just my logo on the back, but open to suggestions) - the overall design is up to you. I want it to be easy to read - not over the top flashy. I already have a company logo which I uploaded so that needs to be used. The colors of my logo are the colors I want on the card... so blue and gray (do need to match the logo colors).

Requirements
Must have
• Would like the card to be sleek, modern and easy to ready

```html
<!DOCTYPE html>
<html lang="en">
<head>
<meta charset="utf-8">
<title>Marrowgate Auctions – Business Cards</title>
<link href="https://fonts.googleapis.com/css2?family=Lato:wght@400;700&display=swap" rel="stylesheet">
<style>
  :root {
    --backdrop: #2b2b2d;
    --card-dark: #161617;
    --card-light: #ffffff;
    --brand-blue: #2a78bd;
    --text-gray: #4a4a4a;
    --soft-gray: #8a8a8a;
  }
  * { margin: 0; padding: 0; box-sizing: border-box; }
  html, body { width: 1200px; height: 716px; overflow: hidden; }
  body {
    background: var(--backdrop);
    font-family: "Lato", sans-serif;
    position: relative;
  }
  .card {
    position: absolute;
    top: 215px;
    width: 500px;
    height: 286px;
    border-radius: 16px;
    overflow: hidden;
    box-shadow: 0 14px 30px rgba(0,0,0,0.45);
  }
  .card-back { left: 70px; background: var(--card-dark); }
  .card-front { left: 630px; background: var(--card-light); }

  .back-brand {
    position: absolute;
    left: 0; right: 0; top: 104px;
    text-align: center;
  }
  .brand-name {
    color: var(--brand-blue);
    font-weight: 700;
    font-size: 30px;
    letter-spacing: 1px;
    text-transform: uppercase;
  }
  .tagline {
    margin-top: 12px;
    color: var(--brand-blue);
    font-size: 13px;
    letter-spacing: 0.3px;
  }

  .front-panel {
    position: absolute;
    left: 0; top: 0; bottom: 0;
    width: 230px;
    background: var(--brand-blue);
    display: flex;
    align-items: center;
    justify-content: center;
    text-align: center;
    padding: 0 20px;
  }
  .front-panel .brand-name {
    color: var(--card-light);
    font-size: 24px;
    line-height: 1.3;
  }
  .contact-block {
    position: absolute;
    left: 262px; top: 70px;
  }
  .person-name {
    color: var(--text-gray);
    font-size: 26px;
    font-weight: 400;
  }
  .person-role {
    color: var(--brand-blue);
    font-size: 14px;
    margin-top: 2px;
  }
  .contact-list {
    list-style: none;
    margin-top: 30px;
  }
  .contact-list li {
    display: flex;
    align-items: center;
    gap: 9px;
    color: var(--text-gray);
    font-size: 14px;
    margin-bottom: 9px;
  }
  .contact-list svg { width: 14px; height: 14px; flex: none; }
</style>
</head>
<body>
  <section class="card card-back">
    <div class="back-brand">
      <div class="brand-name">Marrowgate Auctions</div>
      <div class="tagline">Improving Charity Auctions Nationwide</div>
    </div>
  </section>

  <section class="card card-front">
    <div class="front-panel">
      <div class="brand-name">Marrowgate Auctions</div>
    </div>
    <div class="contact-block">
      <div class="person-name">Owen Hartley</div>
      <div class="person-role">Auctioneer</div>
      <ul class="contact-list">
        <li>
          <svg viewBox="0 0 16 16" aria-hidden="true"><path fill="#2a78bd" d="M3 1h3l1.5 4-2 1.3a9 9 0 0 0 4.2 4.2L11 8.5l4 1.5v3c0 1-1 2-2 2A13 13 0 0 1 1 3c0-1 1-2 2-2z"/></svg>
          02-555-0148
        </li>
        <li>
          <svg viewBox="0 0 16 16" aria-hidden="true"><rect x="1" y="3" width="14" height="10" rx="1" fill="#2a78bd"/><path d="M1.5 4l6.5 5 6.5-5" fill="none" stroke="#fff" stroke-width="1.3"/></svg>
          office@marrowgatemail.com
        </li>
        <li>
          <svg viewBox="0 0 16 16" aria-hidden="true"><g fill="none" stroke="#2a78bd" stroke-width="1.3"><circle cx="8" cy="8" r="6.5"/><ellipse cx="8" cy="8" rx="3" ry="6.5"/><path d="M1.5 8h13M2.5 4.8h11M2.5 11.2h11"/></g></svg>
          bidrevive.com
        </li>
      </ul>
    </div>
  </section>
</body>
</html>
```